Build a Website for refrigeration

7 page web site for refrigeration

Please feel free to use images from our supplier website http://www.norvekcold.com/en/refrigeration
and
http://www.brundalechill.co.uk/

Only websites with images from the above will be accepted

```html
<!DOCTYPE html>
<html lang="en">
<head>
<meta charset="utf-8">
<title>Refrigeration</title>
<link rel="stylesheet" href="https://fonts.googleapis.com/css2?family=Arimo:wght@400;700&display=swap">
<style>
:root{
  --ink:#111;
  --text:#333;
  --muted:#666;
  --link:#1a5a8a;
  --line:#d8d8d8;
  --band:#f4f4f4;
  --red:#cc0000;
  --grey-btn:#e2e2e2;
}
*{box-sizing:border-box;margin:0;padding:0}
html,body{width:1200px;height:1072px;overflow:hidden;background:#fff}
body{position:relative;font-family:"Arimo",Arial,sans-serif;color:var(--text)}
.abs{position:absolute}
.top-links{top:35px;right:143px;display:flex;gap:15px;font-size:10.5px;color:var(--link)}
.brand{left:153px;top:52px;font-size:40px;font-weight:700;color:var(--ink);letter-spacing:-0.5px}
.nav-band{left:0;top:133px;width:1200px;height:36px;border-top:1px solid var(--line);border-bottom:1px solid var(--line);background:#fff}
.nav{left:144px;top:133px;height:36px;display:flex;font-size:12px;font-weight:700;color:var(--ink)}
.nav span{line-height:36px;text-align:center;border-left:1px solid var(--line)}
.nav .feature{width:72px}
.nav .ice{width:174px}
.nav .pastry{width:154px;border-right:1px solid var(--line)}
.nav .empty{line-height:1;padding:5px 0 0 1px;font-size:11.5px;border-left:none;text-align:left}
.search-band{left:0;top:169px;width:1200px;height:38px;background:var(--band);border-bottom:1px solid var(--line)}
.field{height:22px;border:1px solid #c8c8c8;background:#fff}
.btn{height:20px;background:var(--grey-btn);border:1px solid #c6c6c6;font-size:11.5px;font-weight:700;color:#555;line-height:18px;padding:0 6px}
.slider{left:144px;top:217px;width:914px;height:354px;border:1px solid var(--line);background:#fff}
.slide-photo{left:0;top:0;width:706px;height:352px;
  background:
    linear-gradient(180deg,rgba(255,255,255,0) 0%,rgba(255,255,255,0) 100%),
    linear-gradient(180deg,#f3f3f3 0%,#ececec 12%,#5e6166 16%,#d9dcdf 22%,#c7a99a 30%,#d56a2e 37%,#b9bcc0 40%,#d7dadd 52%,#aeb4ba 60%,#f1f1ef 68%,#e6dcc8 76%,#9aa0a6 83%,#3a2a26 90%,#5b4a44 93%,#ededed 97%,#f4f4f4 100%)}
.slide-title{left:728px;top:125px;font-size:35px;font-weight:700;color:var(--ink)}
.slide-sub{left:728px;top:162px;font-size:12.5px;font-weight:700;color:var(--ink)}
.dots{left:768px;top:323px;display:flex;gap:8px}
.dots span{width:19px;height:19px;background:var(--red);color:#fff;font-size:11px;text-align:center;line-height:19px}
.thumb{top:596px;width:155px;height:180px;border:1px solid #ddd;box-shadow:0 2px 4px rgba(0,0,0,.25)}
.t1{left:175px;background:linear-gradient(180deg,#d4d4d4 0%,#e8ecef 18%,#c9d3d8 32%,#9a6a45 48%,#8a5430 70%,#b07a4f 90%,#d8d8d8 100%)}
.t2{left:347px;background:linear-gradient(180deg,#fbfbfb 0%,#c9ccce 20%,#e6d6c4 38%,#d8c3ae 55%,#e6c21f 65%,#e2b90f 85%,#a9acae 92%,#f4f4f4 100%)}
.t3{left:519px;background:linear-gradient(180deg,#fbfbfb 0%,#c4c7c9 18%,#dcc8b4 35%,#cfb59c 52%,#b8bcc0 60%,#c91f25 68%,#b7151c 88%,#f4f4f4 100%)}
.t4{left:691px;background:linear-gradient(180deg,#f0f0f0 0%,#e8ebed 30%,#cfe3ea 45%,#bcd6de 55%,#eef0f1 65%,#d9dcde 85%,#f2f2f2 100%)}
.t5{left:863px;background:linear-gradient(160deg,#8e8a88 0%,#e8d3d3 25%,#d49aa0 45%,#f1e3dc 60%,#c86e74 78%,#e6c8c6 100%)}
.caption{top:796px;width:155px;text-align:center;font-size:12.5px;color:#555}
.view-store{left:961px;top:845px;width:86px;height:26px;background:var(--red);color:#fff;font-size:11.5px;line-height:26px;text-align:center}
.rule{left:144px;width:914px;height:1px;background:var(--line)}
.foot-h{top:902px;font-size:13px;color:var(--link)}
.social{left:163px;top:936px;display:flex;flex-direction:column;gap:10px;font-size:12px;color:#555}
.social div{display:flex;align-items:center;gap:6px;height:17px}
.social i{display:block;width:16px;height:16px;background:#3b5a9a}
.call{left:486px;top:932px;font-size:21px;color:#999}
.phone{left:486px;top:958px;font-size:21px;color:#555}
.hours{left:487px;top:990px;font-size:11px;font-weight:700;color:#555;line-height:18px}
.copy{left:733px;top:903px;font-size:11px;color:#444}
.badge{height:21px;border:1px solid #ccc;background:#e9ecef}
</style>
</head>
<body>
<div class="abs top-links"><span>Home</span><span>About Us</span><span>Contact Us</span><span>Terms &amp; Conditions</span><span>Privacy Policy</span></div>
<div class="abs brand">Refrigeration</div>

<div class="abs nav-band"></div>
<div class="abs nav"><span class="feature">Feature</span><span class="ice">Ice cream display cabinets</span><span class="pastry">Pastry display cabinets</span><span class="empty">No categories</span></div>

<div class="abs search-band"></div>
<svg class="abs" style="left:145px;top:183px" width="15" height="11" viewBox="0 0 15 11"><rect x=".5" y=".5" width="14" height="10" fill="none" stroke="#999"/><path d="M.5 .5 7.5 6 14.5 .5" fill="none" stroke="#999"/></svg>
<div class="abs field" style="left:163px;top:177px;width:140px"></div>
<div class="abs btn" style="left:313px;top:178px">go ›</div>
<div class="abs" style="left:813px;top:182px;font-size:12px;color:#333">Search</div>
<div class="abs field" style="left:860px;top:177px;width:127px"></div>
<div class="abs btn" style="left:991px;top:178px">search ›</div>

<section class="abs slider">
  <div class="abs slide-photo" role="img" aria-label="Curved refrigerated deli display counter with a back counter shelving unit"></div>
  <div class="abs slide-title">ARC</div>
  <div class="abs slide-sub">Back counter plugin</div>
  <div class="abs dots"><span>1</span><span>2</span><span>3</span><span>4</span><span>5</span></div>
</section>

<div class="abs thumb t1" role="img" aria-label="Ice cream display cabinet with brown branded front"></div>
<div class="abs thumb t2" role="img" aria-label="Pastry display cabinet with yellow base"></div>
<div class="abs thumb t3" role="img" aria-label="Pastry display cabinet with red base"></div>
<div class="abs thumb t4" role="img" aria-label="White curved glass gelato display"></div>
<div class="abs thumb t5" role="img" aria-label="Close-up of gelato trays in a display cabinet"></div>
<div class="abs caption" style="left:175px">Refrigerated Brand...</div>
<div class="abs caption" style="left:347px">Duetto</div>
<div class="abs caption" style="left:519px">Quadra</div>
<div class="abs caption" style="left:691px">Lunetta</div>
<div class="abs caption" style="left:863px">Stella</div>
<div class="abs view-store">View Store »</div>

<div class="abs rule" style="top:891px"></div>
<div class="abs foot-h" style="left:163px">Connect with us</div>
<div class="abs foot-h" style="left:335px">Other Links</div>
<div class="abs foot-h" style="left:487px">Live Help</div>
<div class="abs social">
  <div><i></i>Friendloop</div>
  <div><i style="background:#4aa3d8"></i>Chirpline</div>
  <div><i style="background:#b22"></i>Vidstream</div>
  <div><i style="background:#e8762b"></i>update via rss</div>
</div>
<div class="abs call">Call Us Toll Free</div>
<div class="abs phone">555-610-40827</div>
<div class="abs hours">Mon-Fri 10-am to 6 pm est<br>Sat-Sub 10-am to 2 pm est</div>
<div class="abs copy">© 2013 Refrigeration All rights reserved.</div>
<div class="abs badge" style="left:735px;top:936px;width:31px;background:#1a3f8f"></div>
<div class="abs badge" style="left:770px;top:936px;width:31px;background:#e3a21a"></div>
<div class="abs badge" style="left:805px;top:936px;width:31px;background:#4d8fcf"></div>
<div class="abs badge" style="left:840px;top:936px;width:31px;background:#f2f2f2"></div>
<div class="abs badge" style="left:876px;top:936px;width:112px;background:#f6f6f6"></div>
<div class="abs badge" style="left:738px;top:969px;width:84px;background:#f6f6f6"></div>
<div class="abs badge" style="left:829px;top:969px;width:45px;background:#f0c23a"></div>
<div class="abs badge" style="left:881px;top:969px;width:58px;background:#e6e3ef"></div>
<div class="abs badge" style="left:946px;top:969px;width:22px;background:#5a3a1a"></div>
<div class="abs rule" style="top:1053px"></div>
</body>
</html>
```